K3 Construction Site Sign

I would like to get a sign designed which would be installed at a construction sign. I would like to incorporate my current logo, font and colors in the sign. The sign would be 30" x 60" (vertical). Would like to keep it clean and simple yet eye catching and sparks interest. I have attached my branding colors. I would like the background to be the branded blue with white text.

```html
<!DOCTYPE html>
<html lang="en">
<head>
<meta charset="utf-8">
<title>K3 Contracting &amp; Development Ltd. – Site Sign</title>
<link href="https://fonts.googleapis.com/css2?family=Poppins:wght@300;400;500;600&display=swap" rel="stylesheet">
<style>
  :root {
    --brand-blue: #2a5a9a;
    --brand-orange: #e9a93f;
    --paper: #ffffff;
    --photo-sky: #9cc0e0;
    --photo-green: #4f7a3a;
    --photo-house: #e8ecef;
  }
  * { margin: 0; padding: 0; box-sizing: border-box; }
  html, body { width: 922px; height: 1200px; overflow: hidden; background: var(--paper); }
  .sign {
    position: relative; width: 922px; height: 1200px;
    background: var(--paper); font-family: "Poppins", sans-serif; overflow: hidden;
  }
  .corner-accent { position: absolute; top: 0; right: 0; }
  .brand {
    position: absolute; left: 66px; top: 92px;
    display: flex; align-items: center; gap: 26px; color: var(--brand-blue);
  }
  .brand-mark { font-size: 104px; font-weight: 600; line-height: 1; letter-spacing: -4px; }
  .brand-name { font-size: 42px; font-weight: 300; line-height: 1.08; letter-spacing: 1px; text-transform: uppercase; }
  .site-photo { position: absolute; left: 0; top: 0; }
  .services-band { position: absolute; left: 0; top: 0; }
  .services {
    position: absolute; left: 74px; top: 708px; list-style: none;
    color: var(--paper); font-size: 29px; font-weight: 400;
  }
  .services li { display: flex; align-items: center; gap: 20px; height: 60px; }
  .bullet { width: 22px; height: 22px; flex: none; }
  .contact { position: absolute; left: 74px; top: 1000px; color: var(--brand-blue); }
  .contact-row { display: flex; align-items: center; gap: 16px; font-weight: 500; }
  .contact-phone { font-size: 70px; letter-spacing: 1px; line-height: 1.2; }
  .contact-web { font-size: 58px; line-height: 1.2; margin-top: 4px; }
  .contact-icon { width: 38px; height: 38px; flex: none; }
</style>
</head>
<body>
<main class="sign">
  <svg class="corner-accent" width="240" height="220" viewBox="0 0 240 220">
    <polygon points="0,0 240,0 240,210" fill="var(--brand-orange)"/>
  </svg>

  <header class="brand">
    <span class="brand-mark">K3</span>
    <span class="brand-name">Contracting &amp;<br>Development Ltd.</span>
  </header>

  <svg class="site-photo" width="922" height="1200" viewBox="0 0 922 1200" role="img" aria-label="Photograph of a white two-storey custom home with a wraparound porch, shrubs and trees">
    <defs>
      <linearGradient id="photoTone" x1="0" y1="0" x2="0" y2="1">
        <stop offset="0" stop-color="var(--photo-sky)"/>
        <stop offset="0.45" stop-color="var(--photo-house)"/>
        <stop offset="1" stop-color="var(--photo-green)"/>
      </linearGradient>
    </defs>
    <polygon points="62,250 860,250 860,720 700,598 62,650" fill="url(#photoTone)"/>
  </svg>

  <svg class="services-band" width="922" height="1200" viewBox="0 0 922 1200">
    <polygon points="0,668 604,612 922,850 922,960 0,968" fill="var(--brand-blue)"/>
  </svg>

  <ul class="services">
    <li><svg class="bullet" viewBox="0 0 22 22"><polygon points="22,0 22,22 0,22" fill="var(--paper)"/></svg>Custom Homes</li>
    <li><svg class="bullet" viewBox="0 0 22 22"><polygon points="22,0 22,22 0,22" fill="var(--brand-orange)"/></svg>Commercial/Retail</li>
    <li><svg class="bullet" viewBox="0 0 22 22"><polygon points="22,0 22,22 0,22" fill="var(--paper)"/></svg>Land Development Consulting</li>
    <li><svg class="bullet" viewBox="0 0 22 22"><polygon points="22,0 22,22 0,22" fill="var(--brand-orange)"/></svg>Construction Project Management</li>
  </ul>

  <section class="contact">
    <div class="contact-row contact-phone">
      <svg class="contact-icon" viewBox="0 0 24 24"><path d="M6.6 10.8a15 15 0 0 0 6.6 6.6l2.2-2.2a1 1 0 0 1 1-.25 11.4 11.4 0 0 0 3.6.57 1 1 0 0 1 1 1V20a1 1 0 0 1-1 1A17 17 0 0 1 3 4a1 1 0 0 1 1-1h3.5a1 1 0 0 1 1 1c0 1.25.2 2.45.57 3.57a1 1 0 0 1-.25 1z" fill="var(--brand-orange)"/></svg>
      <span>1 604-555-0182</span>
    </div>
    <div class="contact-row contact-web">
      <svg class="contact-icon" viewBox="0 0 24 24"><circle cx="12" cy="12" r="10" fill="var(--brand-orange)"/><path d="M2 12h20M12 2c3 3 3 17 0 20M12 2c-3 3-3 17 0 20" stroke="var(--paper)" stroke-width="1.4" fill="none"/></svg>
      <span>K3contracting.com</span>
    </div>
  </section>
</main>
</body>
</html>
```